Business card design needed to incorporate existing logo

We need a business card for a new modern Accounting & Business Solutions company call KelvaTrade Services.com.au servicing all of Australia.
My tagline is Steady Ledger Answers... built right.

We specialise in Cloud Accounting and this is our primary focus. We also provide tax representation, debt recovery, computer, tablet and smart phone sales.

I would like a design that uses my corporate, trustworthy colours of blue/white, black/grey however am open to suggestion. I have attached my logo to go on the card somewhere,of which you will see the colour scheme.

I am after a card that STANDS OUT, somewhere between it not being too busy and not being a baron waste of space.

A 'cloud' incorporated in the design may work well, up to your artistic judgement. I know what I like when I see it; it is harder to put into words!

Excited to see your ideas!
I have added my logo predominately (blue/white) and for additional opportunity have added my reverse logo (darker one). I have used the blue/white on my website and letterhead. I will be using both on my vehicle signage.

Target Market(s)

Tradesmen and small-medium businesses of all descriptions Australia-wide

Industry/Entity Type

Debt

Contact Information for Business Card

Dale Pemberton
Principal (optional)
KelvaTrade Services.com.au
Steady Ledger Answers... built right

P: 1800 513 684
M: 0412 860 571 (optional)
W: www.kelvatradeservices.com.au
E: admin@kelvatradeservices.com.au

Logo Text

Steady Ledger Answers... built right!

Logo styles of interest
Wordmark Logo
Requirements
Must have
• Must look professional and of high quality not cheap.

My logo and my tagline 'Steady Ledger Answers... built right'.

I have my colourscheme in mind as per my attached logo, however am open to suggestion. I want to see what you can create that I would not have thought of.

Modern, innovative.
Something I won't look at and think, 'I could have done that myself'.

Must be able to be printed on Norla 300gm premium cards and the artwork provided to me.
Nice to have
• Title of Principal is optional depending on space and judement call of look/fee.
M: (mobile) number is also optional as above.

Somthing cloud related given the Cloud Accounting aspect may be relevant. I leave it to your artistic design and judgement.
Should not have
• Must not look cheap.

```html
<!DOCTYPE html>
<html lang="en">
<head>
<meta charset="utf-8">
<title>KelvaTrade Services – Business Card</title>
<link rel="stylesheet" href="https://fonts.googleapis.com/css2?family=Questrial&family=Montserrat:wght@700&display=swap">
<style>
  :root {
    --navy: #1b2859;
    --navy-deep: #15214c;
    --sky: #3f93d3;
    --paper-light: #fbfbfb;
    --paper-mid: #e6e6e7;
    --paper-shade: #cfd0d2;
    --ink: #1f1f24;
    --ink-soft: #4a4a50;
    --backdrop: #8e8e90;
  }
  * { box-sizing: border-box; margin: 0; padding: 0; }
  html, body {
    width: 1200px; height: 1200px; overflow: hidden;
    background: var(--backdrop);
    font-family: "Questrial", "Century Gothic", sans-serif;
  }
  .canvas {
    width: 1200px; height: 1200px;
    display: flex; flex-direction: column; align-items: center; justify-content: center;
    gap: 60px;
  }
  .card {
    position: relative;
    width: 820px; height: 500px;
    overflow: hidden;
    box-shadow: 0 10px 28px rgba(0,0,0,.28);
  }

  /* Back side */
  .card--back {
    background: linear-gradient(160deg, var(--paper-light) 0%, var(--paper-mid) 70%, var(--paper-shade) 100%);
  }
  .back-band {
    position: absolute; left: 0; right: 0; top: 140px; height: 150px;
    background: var(--navy);
    display: flex; align-items: center; justify-content: center;
  }
  .back-band::after {
    content: ""; position: absolute; left: 0; right: 0; top: 150px; height: 14px;
    background: linear-gradient(to bottom, rgba(60,60,66,.55), rgba(60,60,66,0));
  }
  .brand-lockup {
    display: flex; align-items: center; gap: 14px;
    color: var(--sky); font-size: 38px; letter-spacing: 2px;
  }
  .brand-dot {
    width: 22px; height: 22px; border-radius: 50%; background: var(--sky);
  }

  /* Front side */
  .card--front {
    background: linear-gradient(160deg, var(--paper-light) 0%, var(--paper-mid) 75%, var(--paper-shade) 100%);
  }
  .front-panel {
    position: absolute; left: 0; top: 0; bottom: 0; width: 345px;
    background: var(--navy);
    color: #fff;
    padding: 78px 20px 0 22px;
    overflow: hidden;
  }
  .panel-mark {
    width: 150px; height: 150px; border-radius: 50%;
    background: var(--sky);
    margin: 0 auto 26px auto;
  }
  .panel-name {
    color: var(--sky); font-size: 22px; letter-spacing: 0; white-space: nowrap;
  }
  .panel-tagline {
    color: #fff; font-size: 16px; margin-top: 4px; white-space: nowrap;
  }
  .holder {
    position: absolute; right: 52px; top: 82px; text-align: left;
  }
  .holder-name {
    font-family: "Montserrat", "Arial", sans-serif; font-weight: 700;
    color: var(--navy); font-size: 30px;
  }
  .holder-title {
    color: var(--ink-soft); font-size: 19px; margin-top: 2px;
  }
  .contact {
    position: absolute; left: 378px; bottom: 78px;
    list-style: none; color: var(--ink); font-size: 20px; line-height: 1.32;
  }
  .contact-label {
    font-family: "Montserrat", "Arial", sans-serif; font-weight: 700;
    display: inline-block; width: 30px; font-size: 17px;
  }
</style>
</head>
<body>
  <main class="canvas">
    <section class="card card--back" aria-label="Card back">
      <div class="back-band">
        <div class="brand-lockup">
          <span class="brand-dot"></span>
          <span class="brand-name">KelvaTrade Services.com.au</span>
        </div>
      </div>
    </section>

    <section class="card card--front" aria-label="Card front">
      <div class="front-panel">
        <div class="panel-mark" aria-hidden="true"></div>
        <p class="panel-name">KelvaTrade Services.com.au</p>
        <p class="panel-tagline">Steady Ledger Answers... built right</p>
      </div>

      <div class="holder">
        <h1 class="holder-name">Dale Pemberton</h1>
        <p class="holder-title">Principal</p>
      </div>

      <ul class="contact">
        <li><span class="contact-label">P :</span>1800 513 684</li>
        <li><span class="contact-label">M:</span>0412 860 571</li>
        <li><span class="contact-label">E :</span>admin@kelvatradeservices.com.au</li>
      </ul>
    </section>
  </main>
</body>
</html>
```